New Snazzy yet professinoal business card updated for todays consumer for a Real Estate Professional

I work in a family owned real estate business where we specialize in sales (buyer/seller) and property management. I would like a snazzy business card that will set me apart from other agents while maintaining its professional appearance. I would like to use the front and back of the card incorporating the business logo on the front with pictures and my personal logo on the back side. I have to have the TBNX symbol which I have attached. Card must be easy to read, distinguishable, and professional. Old card with contact information attached. My email has changed to Milo@MiloHathawayHomes.com

Target Market(s)

Home Sellers, Home Buyers, Business Professionals, Marketing Services,

Industry/Entity Type

Real Estate Agent

Contact Information for Business Card

Professional business card to stand apart from other agents while maintaining a professional appeal.

Font styles to use
Serif

Colors
ec1f27
fbee3e
0455a3

Requirements
Must have
• Must have contact information clear, easy to read. legible
Nice to have
• My picture.

```html
<!DOCTYPE html>
<html lang="en">
<head>
<meta charset="utf-8">
<title>Milo Hathaway Homes – Business Card</title>
<link rel="stylesheet" href="https://fonts.googleapis.com/css2?family=Arimo:wght@400;700&display=swap">
<style>
  :root {
    --page: #e9e7e3;
    --navy: #1d2b85;
    --royal: #2c46b5;
    --brand-blue: #1f3b9c;
    --brand-red: #d92a35;
    --ink: #5a5a5a;
    --grey: #8a8a8a;
    --white: #ffffff;
    --photo-a: #c9c4bb;
    --photo-b: #8e8a84;
  }
  * { box-sizing: border-box; margin: 0; padding: 0; }
  html, body { width: 1200px; height: 950px; overflow: hidden; }
  body {
    background: var(--page);
    font-family: "Arimo", Arial, sans-serif;
    display: flex; flex-direction: column; align-items: center; justify-content: center;
    gap: 50px;
  }
  .card {
    position: relative; width: 700px; height: 400px; overflow: hidden;
    box-shadow: 0 8px 24px rgba(0,0,0,.18);
  }
  /* back side */
  .card-back {
    background: linear-gradient(135deg, var(--royal) 0%, var(--navy) 100%);
    color: var(--white);
    display: flex; flex-direction: column; align-items: center; justify-content: center;
  }
  .back-brand { display: flex; align-items: center; gap: 14px; }
  .back-brand .dot { width: 22px; height: 22px; border-radius: 50%; background: var(--white); }
  .back-brand .name { font-size: 30px; font-weight: 400; letter-spacing: 1px; }
  .back-web { margin-top: 40px; font-size: 14px; letter-spacing: 4px; }

  /* front side */
  .card-front { background: var(--white); }
  .swoosh { position: absolute; inset: 0; }
  .brand { position: absolute; left: 30px; top: 42px; display: flex; align-items: center; gap: 12px; }
  .brand .dot { width: 36px; height: 36px; border-radius: 50%; background: var(--brand-red); }
  .brand .words { display: flex; flex-direction: column; align-items: flex-end; }
  .brand .name { font-size: 30px; color: var(--brand-blue); line-height: 1; }
  .brand .sub { font-size: 14px; color: var(--grey); letter-spacing: 6px; margin-top: 4px; }
  .address { position: absolute; left: 30px; top: 130px; font-size: 15px; color: var(--ink); line-height: 21px; }
  .badge { display: inline-block; width: 30px; height: 14px; border-radius: 3px; background: #9fb8e6; vertical-align: middle; margin-left: 8px; }
  .contacts { position: absolute; left: 30px; top: 182px; list-style: none; font-size: 15px; color: var(--ink); }
  .contacts li { display: flex; align-items: center; gap: 10px; height: 24px; }
  .contacts svg { width: 15px; height: 15px; fill: var(--navy); }
  .photo {
    position: absolute; left: 430px; top: 18px; width: 232px; height: 180px; border-radius: 18px;
    background: radial-gradient(circle at 50% 40%, var(--photo-a), var(--photo-b));
  }
  .agent { position: absolute; right: 38px; top: 208px; text-align: right; }
  .agent .name { font-size: 21px; font-weight: 700; color: var(--brand-blue); }
  .agent .title { font-size: 16px; color: var(--brand-red); margin-top: 2px; }
</style>
</head>
<body>
  <section class="card card-back">
    <div class="back-brand"><span class="dot"></span><span class="name">MILO HATHAWAY</span></div>
    <div class="back-web">www.website.com</div>
  </section>

  <section class="card card-front">
    <svg class="swoosh" viewBox="0 0 700 400" preserveAspectRatio="none" aria-hidden="true">
      <path d="M0,362 C220,352 500,327 700,277 L700,400 L0,400 Z" fill="var(--navy)"/>
      <path d="M0,354 C220,344 500,319 700,269" fill="none" stroke="var(--white)" stroke-width="6"/>
      <path d="M0,346 C220,336 500,311 700,261" fill="none" stroke="var(--brand-red)" stroke-width="6"/>
    </svg>

    <div class="brand">
      <span class="dot"></span>
      <div class="words"><span class="name">MILO HATHAWAY</span><span class="sub">HOMES</span></div>
    </div>

    <p class="address">48 Larkmoor court glenbrook<br>Mississippi 39177<span class="badge"></span></p>

    <ul class="contacts">
      <li><svg viewBox="0 0 24 24"><path d="M6.6 10.8a15 15 0 0 0 6.6 6.6l2.2-2.2a1 1 0 0 1 1-.25 11 11 0 0 0 3.6.6 1 1 0 0 1 1 1V20a1 1 0 0 1-1 1A17 17 0 0 1 3 4a1 1 0 0 1 1-1h3.5a1 1 0 0 1 1 1 11 11 0 0 0 .6 3.6 1 1 0 0 1-.25 1z"/></svg>601.555.0142</li>
      <li><svg viewBox="0 0 24 24"><path d="M7 1h10a2 2 0 0 1 2 2v18a2 2 0 0 1-2 2H7a2 2 0 0 1-2-2V3a2 2 0 0 1 2-2zm0 3v15h10V4z"/></svg>601.555.0178</li>
      <li><svg viewBox="0 0 24 24"><path d="M6 2h10v5H6zM4 8h16a2 2 0 0 1 2 2v7h-4v5H6v-5H2v-7a2 2 0 0 1 2-2zm4 9v3h8v-3z"/></svg>601.555.0193</li>
      <li><svg viewBox="0 0 24 24"><path d="M2 5h20v14H2zm2 2v.5l8 5 8-5V7z"/></svg>Milo@MiloHathawayHomes.com</li>
    </ul>

    <div class="photo" role="img" aria-label="Portrait photo of the agent"></div>
    <div class="agent">
      <div class="name">Milo Hathaway</div>
      <div class="title">Realtor, MBA, MPH</div>
    </div>
  </section>
</body>
</html>
```